Web Design Project for NFYL

Hi,
I am looking for a website design for the Northern Federation of Youth Listeners.
This is an organisation which helps with legal disputes and other challenges which involve children.  The company want a web page which is professional but friendly.  The purpose of the website is to explain what the organisation does and to give people a place where they can download documents and information.
The homepage will have a video on the page.  ALSO, we would prefer the site to have a left hand navigation (not a top navigation).
I have enclosed the logo, a picture of the old (rubbish) home page and a screenshot from the video (you are welcome to change the dimensions).
If you have any questions, please ask.
-D
UPDATE: 6th DECEMBER:
Thanks for the designs so far.  I promise to give feedback to every single person.  In the meantime, can I just say that there's some good designs so far but I don't think anyone has nailed this yet.
So, I am uploading a screenshot called "theylikethis.jpg".  This is a screenshot from a website that the client says they like.
Can I also say, it's okay to reduce the size of the video.  I'm seeing a lot of massive videos.
Thanks folks!
UPDATE:  You can view a live demo of the site that they like at www.demohostqv.co.uk
UPDATE:  I've just found another good example of a site with a left nav at www.brightpathresourcehub.com

Updates
Hi,
Hi folks,
Had a quick look at the designs and just to say how impressed I am with the qualityand choice. There are a few that caught my eye and I'll try and narrow them down.I've also passed the link onto the other representatives for their input beforemaking a final choice. If I don't hear from any of the other represenatatives by Wednesday, I'll chose adesign and let you know. Once again many thanks for the quick response in gettingdesigns done and really looking forward to seeing the completed website.
Industry/Entity Type
Legal
Requirements
Must have
- a video player (any size of your choosing)
a left side navigation
the logo

```html
<!DOCTYPE html>
<html lang="en">
<head>
<meta charset="utf-8">
<title>Northern Federation of Youth Listeners</title>
<link rel="stylesheet" href="https://fonts.googleapis.com/css2?family=Arimo:wght@400;700&family=Cinzel+Decorative:wght@900&family=Ubuntu:wght@400;500&family=Yanone+Kaffeesatz:wght@400;600&display=swap">
<style>
:root{
  --navy:#0b3a96;
  --royal:#1250c4;
  --sky:#e9f1fb;
  --page:#e6e6e6;
  --panel:#f3f3f3;
  --sidebar:#e2e2e2;
  --text:#333;
  --accent:#cc2200;
  --white:#fff;
  --gold:#f3d27a;
}
*{box-sizing:border-box;margin:0;padding:0}
html,body{width:1124px;height:1200px;overflow:hidden}
body{font-family:"Ubuntu",Verdana,sans-serif;color:var(--text);background:var(--page);position:relative}
.abs{position:absolute}
.header{left:0;top:0;width:1124px;height:108px;background:linear-gradient(#dce9f8,#f8fbfe 60%,#fff)}
.brand-mark{left:173px;top:42px;width:40px;height:40px;background:var(--navy)}
.brand-name{left:221px;top:49px;font:500 22px "Ubuntu",sans-serif;color:var(--navy)}
.site-title{left:300px;top:26px;width:590px;font:900 27px/34px "Cinzel Decorative",serif;color:var(--navy)}
.site-title span{display:block}
.site-title span+span{text-align:right}
.hero-band{left:0;top:108px;width:1124px;height:233px;background:linear-gradient(#083a9c,#0e4bc0 40%,#1560d8 85%,#3b80e6);border-top:3px solid var(--navy)}
.hero-photo{left:169px;top:111px;width:786px;height:228px;background:linear-gradient(100deg,#d6dde3,#b79c82 35%,#e3d6c4 60%,#9d8a77);border:3px solid var(--navy)}
.body-area{left:167px;top:341px;width:789px;height:659px;background:var(--panel);border-left:1px solid #d0d0d0;border-right:1px solid #d0d0d0}
.sidebar{left:167px;top:341px;width:197px;height:659px;background:var(--sidebar);border-right:1px solid #cfcfcf}
.nav{left:167px;top:352px;width:188px;list-style:none}
.nav li{height:26px;margin-bottom:8px;background:linear-gradient(90deg,#0a2f86 0,#2f6fe0 3%,#0e45b8 12%,#1657d0 60%,#0d45b5);border-left:4px solid #06246e;font:400 12.5px/26px "Arimo",sans-serif;color:var(--white);padding-left:35px}
.news-box{left:173px;top:686px;width:181px;height:287px;background:var(--white);border:1px solid #cfcfcf}
.news-head{left:173px;top:677px;width:170px;height:29px;background:linear-gradient(90deg,#0a48c0,#1e8cf0 70%,#3bb4f8);clip-path:polygon(0 0,100% 0,92% 50%,100% 100%,0 100%);font:500 16px/29px "Yanone Kaffeesatz",sans-serif;color:var(--white);padding-left:30px;letter-spacing:.3px}
.news-item{left:180px;width:168px;height:85px}
.date{position:absolute;left:0;top:0;width:48px;height:49px;border:1px solid var(--navy);text-align:center;font-family:"Ubuntu",sans-serif}
.date b{display:block;height:24px;background:var(--navy);color:var(--white);font:400 16px/24px "Ubuntu",sans-serif}
.date i{display:block;height:23px;background:linear-gradient(#5fa4ee,#8cc4f6);color:var(--white);font:normal 14px/23px "Ubuntu",sans-serif;letter-spacing:1px}
.news-item p{position:absolute;left:59px;top:0;width:108px;font-size:10px;line-height:12.5px}
.news-more{position:absolute;right:5px;top:62px;font:700 8px "Arimo",sans-serif;color:var(--accent)}
.news-rule{left:182px;width:158px;border-top:1px dashed #555}
h1.welcome{left:396px;top:361px;font:400 20px "Ubuntu",sans-serif;color:var(--navy);white-space:nowrap}
.intro{left:396px;top:389px;width:364px;font-size:10.4px;line-height:15px;text-align:justify;letter-spacing:.2px}
.learn{left:689px;top:533px;font:700 9px "Arimo",sans-serif;color:var(--accent);display:flex;align-items:center;gap:5px}
.learn svg{width:11px;height:11px}
.frame{left:789px;top:393px;width:152px;height:149px;background:#c8561c;border:2px solid #a8400f;padding:9px}
.frame div{width:100%;height:100%;background:linear-gradient(135deg,#b7b1a9,#e9dccf 50%,#c38a7a);border:1px solid #7a2d0a}
.video{left:396px;top:558px;width:366px;height:228px;background:linear-gradient(#ddd,#8c8c8c);padding:6px;box-shadow:2px 3px 4px rgba(0,0,0,.35)}
.video-still{width:100%;height:100%;background:radial-gradient(ellipse at 50% 55%,#c99f88 0,#8a5a44 35%,#e9e9e9 65%,#f4f4f4);position:relative}
.play{position:absolute;left:154px;top:80px;width:61px;height:40px}
.download{left:789px;top:559px;width:152px;height:222px;background:linear-gradient(#1557c2,#0b3b94 60%,#062b77)}
.download svg{position:absolute;left:15px;top:2px}
.download p{position:absolute;left:0;width:152px;text-align:center;font-family:"Yanone Kaffeesatz",sans-serif;color:#cfe3fb}
.dl1{top:24px;font-size:24px;font-weight:400;color:#a9cdf2 !important}
.dl2{top:61px;font-size:25px;font-weight:600;color:var(--gold) !important;letter-spacing:.5px}
.dl3{top:102px;font-size:20px;line-height:21px}
h2.sec{font:400 16px "Ubuntu",sans-serif;color:#222;letter-spacing:.4px}
.obj-title{left:395px;top:804px}
.obj-text{left:395px;top:822px;width:546px;font-size:10.4px;line-height:15px;text-align:justify;letter-spacing:.2px}
.mem-title{left:395px;top:898px}
.members{left:396px;top:922px;width:540px;height:60px;background:linear-gradient(160deg,#f6f6f6,#e2e2e2);border:1px solid #cfcfcf;border-radius:3px}
.member{top:928px;width:62px;height:48px;background:var(--navy)}
.footer{left:0;top:1000px;width:1124px;height:168px;background:var(--navy)}
.footer h3{position:absolute;font:400 14.5px "Ubuntu",sans-serif;color:var(--white)}
.sitemap{left:190px;top:1035px;list-style:none;font-size:10.6px;line-height:13.3px;color:#dbe6fb;letter-spacing:.8px}
.contact{left:465px;top:1035px;font-size:10.6px;color:#dbe6fb;letter-spacing:.5px}
.contact dt{position:absolute;left:0}
.contact dd{position:absolute;left:56px;width:160px;line-height:15px}
.social{width:36px;height:36px;border-radius:6px;background:#eef3fb;opacity:.95}
.copy{left:0;top:1168px;width:1124px;height:32px;background:#0a3185;border-top:1px solid #4a70bf;text-align:center;font:400 9px/30px "Ubuntu",sans-serif;color:#d4def5}
</style>
</head>
<body>
<header>
  <div class="abs header"></div>
  <div class="abs brand-mark"></div>
  <div class="abs brand-name">NFYL</div>
  <div class="abs site-title"><span>Northern Federation of</span><span>Youth Listeners</span></div>
  <div class="abs hero-band"></div>
  <div class="abs hero-photo" role="img" aria-label="Photo of smiling children on a beach"></div>
</header>

<div class="abs body-area"></div>
<aside class="abs sidebar"></aside>
<ul class="abs nav">
  <li>Home</li><li>About Us</li><li>News</li><li>Conferences</li><li>Minutes</li><li>Annual Report</li><li>Archive</li><li>Contact Us</li><li>Links</li>
</ul>

<div class="abs news-box"></div>
<div class="abs news-head">News</div>
<div class="abs news-item" style="top:720px"><div class="date"><b>DEC</b><i>30</i></div><p>Lorem ipsum dolor amet, consectetur adipiscing elit. Duis purus tellus, quis</p><span class="news-more">Learn more →</span></div>
<div class="abs news-rule" style="top:793px"></div>
<div class="abs news-item" style="top:805px"><div class="date"><b>DEC</b><i>30</i></div><p>Lorem ipsum dolor amet, consectetur adipiscing elit. Duis purus tellus, quis</p><span class="news-more">Learn more →</span></div>
<div class="abs news-rule" style="top:881px"></div>
<div class="abs news-item" style="top:890px"><div class="date"><b>DEC</b><i>30</i></div><p>Lorem ipsum dolor amet, consectetur adipiscing elit. Duis purus tellus, quis</p><span class="news-more" style="top:64px">Learn more →</span></div>

<main>
  <h1 class="abs welcome">Welcome to Northern Federation of Youth Listeners</h1>
  <p class="abs intro">Lorem ipsum dolor sit amet, consectetuer adipiscing elit. Nam cursus. Morbi ut mi. Nullam enim leo, egestas id, condimentum at, laoreet mattis, massa. Sed eleifend nonummy diam. Praesent mauris ante, elementum et, bibendum at, posuere sit amet, nibh. Duis tincidunt lectus quis dui viverra vestibulum. Suspendisse vulputate aliquam dui. bibendum at, posuere sit amet, nibh. Duis tincidunt lectus quis dui viverra vestibulum. Suspendisse vulputate aliquam dui. posuere sit amet, nibh. Duis tincidunt lectus quis dui viverra vestibulum. Suspendisse vulputate aliquam dui.</p>
  <div class="abs learn"><svg viewBox="0 0 12 12"><circle cx="6" cy="6" r="5.3" fill="#f4f4f4" stroke="#999"/><path d="M5 3.5 8 6 5 8.5z" fill="#666"/></svg>Learn more</div>
  <div class="abs frame"><div role="img" aria-label="Photo of a young girl resting her chin on her hands"></div></div>

  <div class="abs video"><div class="video-still" role="img" aria-label="Video still of a smiling woman speaking to camera">
    <svg class="play" viewBox="0 0 61 40"><rect width="61" height="40" rx="8" fill="#111"/><path d="M24 10 42 20 24 30z" fill="#fff"/></svg>
  </div></div>

  <div class="abs download">
    <svg width="122" height="212" viewBox="0 0 122 212"><defs><linearGradient id="rib" x1="0" y1="0" x2="0" y2="1"><stop offset="0" stop-color="#1f78d8"/><stop offset="1" stop-color="#0c4fb4"/></linearGradient></defs><path d="M2 0H120V172L61 210 2 172Z" fill="url(#rib)" stroke="#4a97e6" stroke-width="1.5"/></svg>
    <p class="dl1">Click to</p>
    <p class="dl2">DOWNLOAD</p>
    <p class="dl3">Documents<br>and<br>Information</p>
  </div>

  <h2 class="abs sec obj-title">Objectives</h2>
  <p class="abs obj-text">Lorem ipsum dolor sit amet, consectetuer adipiscing elit. Nam cursus. Morbi ut mi. Nullam enim leo, egestas id, condimentum at, laoreet mattis, massa. Sed eleifend nonummy diam. Praesent mauris ante, elementum et, bibendum at, posuere sit amet, nibh. Duis tincidunt lectus quis dui viverra vestibulum. Suspendisse vulputate aliquam dui.</p>

  <h2 class="abs sec mem-title">Our Members</h2>
  <div class="abs members"></div>
  <div class="abs member" style="left:410px"></div>
  <div class="abs member" style="left:486px"></div>
  <div class="abs member" style="left:562px"></div>
  <div class="abs member" style="left:638px"></div>
  <div class="abs member" style="left:714px"></div>
  <div class="abs member" style="left:789px"></div>
  <div class="abs member" style="left:859px"></div>
</main>

<footer>
  <div class="abs footer">
    <h3 style="left:188px;top:10px">Sitemap</h3>
    <h3 style="left:465px;top:10px">Contact Info</h3>
    <h3 style="left:797px;top:7px">Lets get social</h3>
  </div>
  <ul class="abs sitemap"><li>Home</li><li>About Us</li><li>News</li><li>Conferences</li><li>Minutes</li><li>Annual Report</li><li>Archive</li><li>Contact Us</li><li>Links</li></ul>
  <dl class="abs contact">
    <dt style="top:0">Address:</dt><dd style="top:0">Lorem ipsum dolor sit amet, consectetuer adipiscing elit. Nam cursus.</dd>
    <dt style="top:56px">Tel:</dt><dd style="top:56px">01632 000 000</dd>
    <dt style="top:83px">Email:</dt><dd style="top:83px">info@nfyl-mail.org</dd>
  </dl>
  <div class="abs social" style="left:801px;top:1055px" aria-label="Social link"></div>
  <div class="abs social" style="left:865px;top:1055px" aria-label="Social link"></div>
  <div class="abs social" style="left:801px;top:1101px" aria-label="Social link"></div>
  <div class="abs social" style="left:865px;top:1101px" aria-label="Social link"></div>
  <div class="abs copy">Copyright © 2012 &nbsp;Northern Federation of Youth Listeners</div>
</footer>
</body>
</html>
```